Web Design Wecangrowbright

Overview: To develop web site with 1 main page and 1 sample inside page. Site already exists, but has been put offline. Content has been fully rewritten. If I like your style, I will pay extra for additional inside pages.
WHO I AM?
www.wecangrowbright.org was originally created to become an online community for people to use my online tools, researches, and findings to learn how to become happier.
Today, my primary services is “health coaching and lifestyle specialist.” I’m a food specialist suggesting customized solutions for my clients to eat better, how to eat, cook, groceries shop, lose weight, reduce craving, and reverse diseases.
My edge is when a suggest food I explain Why such food hurts them (or make them sick –or reason of diseases) or how the food I suggest can heal them, strengthen them, or make them lose weight. My connection to food is medical and directly impacts my client’s health.
I want to be seen as a professional in clinical nutrition and as a guru in overall wellbeing.
I coach my clients’ lifestyle as a WHOLE, introducing them to new food, fitness, and teaching them techniques to better cope with life. I study their overall health, history, and treatments, diseases, allergies as a WHOLE, connecting all medical specialties.
My services:
I sell coaching sessions, for 1 hour, 2/month for a total program of 6 months. During the sessions, I not only coach client on nutrition, but also on career, relationship, fitness, goals, and the reasons why people can’t achieve their dreams, or how to remove stress or re-organize their lives.
Future services: I may want to sell products such as T-shirts and other promotional items
Payment methods: Since I sell, I’ll need paypal and credit card payment on line. I accept checks as well (they can find my address on “contact us”)
More services, near future:
As a Certified personal fitness Trainer, I will soon offer circuit training (outdoors) and boot camps in the neighborhood to get people moving, at very affordable prices. The goal of those events will be to grow my wecangrowbright community and get new clients for Health coaching.
Knowledgeable about controlling the mind, anger, and stress, I will soon offer group meditations and breathing sessions .
Objectives:
The goal of the site are:
• To entice visitors to become my clients. The look of the site needs to reflect my customized services.
• To offer to spend an hour with client for a free health history.
• To post videos about cooking videos, discussing a theme (sugar craving, which Carbs is good for me?)
• After I meet people and give them my business cards, as they visit my site, they needs to feel impressed by the caliber of expertise.
Schedules and Budget:
Target due date is 1 week from submission of my project. During that phase, I’d like to see a wireframe, colors, styles, incorporating my logo, suggesting pictures. I would like designed tabs, access to videos, and photo library.
Motivations for people to become CLIENTS:
I think what would make people want to get my services is if they see me as an expert in holistic weight loss, someone that they can share their life, thrust, and speak at length without being judged. Visuals are crucial to simply explain effect of food on the body (needs videos main page and archive videos on various topics)
Overall, the emotions we can play with - (key words) feeling energized, feeling strong, in control of your life, a holitistic approach to a new healthy lifestyle, Balance mind, fitness, and diet, take responsibility for your own life, feeling lighter, happier, more peaceful.
Key issues of my clients:
Weight issues, high blood pressure, depression, anxiety, stress, don’t know and what to cook, suffer from diabetes, celiac, digestive diseases. People are fatigued or can’t sleep. They are addicted to sugar, coffee, fast food, speedy life.
Another issue is finding time to eat better, making exercise a routine, making the time to remove stress and enjoy life.
How do I solve clients’ problems?:
Rather than being treated by various medical specialists, I look over their Overall health since childhood. I try to find triggers of their sicknesses that often originate from their lifestyle (stress, lack of exercise, eating junk, allergies) and I recommend life modification, introduce new food, exercise , and help them shuffle their lives around. My approach is extremely customized and always requires Hours of research on my side to fully guide a client.
Demographics:
Teenagers, singles, families, young mothers. Most of clients come with weight issues, some may come to reduce cravings.
Key Messages:
The main page (please find attached “wireframe”) shall give the visitor a sense he found the guru in holistic health. Whatever medical concern they have or struggle will finally be taken care of. Someone loves them and truly cares. Food knowledge is medical, flavor, and based on client’s own taste and willingness to try. The overall feel needs to be sleek and professional.
Call to Action
Ideally, I want people to e-mail me their filled up health history (can download blank men or women health history form) so I can schedule an appointment with them (the best solution for me)
People can also call me. Since calling me is for general questions about my program, I would prefer the e-mail version whereby clients send me their health history.
Creative Considerations
Layout – considerations in accordance to brand guidelines
Need suggetions!
Tone –
Expert in clinical food and holistic health.
Visual
Color palette : I’m not sure, but the background could be light gray (clinical health), golden desert, sahara desert, earthy, pottery (well being) warm colors (orange to warm brown) or other suggestion?
Photography: I thought about flash picture. 1 picture as banner with a message on it. About 3 pictures rotate randomly.
Picture A: is “holistic food, green vegetables, natural edible roots, or cruciferous vegetables, a platter of fresh fruits and vegies, or fresh market (spices, roots, fruits and vegies). Picture needs to be crisp clear.
Picture B: Ideally: a lady fitness trainer training group exercise outdoors, in a park, or a group of people exercising outside, people look happy, boot camp training, circuit training as a group
Picture C: a picture representing the soul ,meditation, a person relaxing next to beach or in forest, next to flowers or lushy plants, a person re-energizing.
Logo: attached as separate files with various backgrounds
Icons: may look cool to use vegies or weight, happy face, or ginger root…
typography, graphics: need suggestions!

Resources
• I have an existing website name “wecangrowbright.org” the site has been put out of internet since we were trying to change it. Let me know if you need to access site. Content of the site is ineffective.
• All content has been written. You can suggest layouts and tabs
Updates

Target Market(s)

My industry is Health care, holistic Health (no medications, no supplements, no surgeries)
Buyer’s Type could be anyone wanting to lose weight, feel better, reduce stress, learn to eat, to cook, to groceries shop. My buyers are confused about all diets.My audience is people WHO WANT change in their lives. Some people know they should eat better, they mostly need support and motivation.
Typical buyer is someone who wants a new chance, a new life!
My primary target buyer is:
1. Family. I wish to coach the entire family into healthier eating and teach them how to cook and eat as a family by changing their habits.
My secondary markets are:
1.Teenagers (often eating emotionally and confused about diets)

Industry/Entity Type

Requirements
Must have
• • Format – web, print, video, sound
I would like videos (youtube connect) – facebook connect – calendar (I will update) – I will update my content, videos, and photo library regularly – people should be able to e-mail me from site – maybe be able to go through web conference. 2 different words or pdf forms shall be available for download or online filling, then they should be able to e-mail forms through site or through their personal mail system. They can also print and mail it to me.
Managing the site:
I would like to upload videos, pictures and text freely and easily. I would like to manage and update content
Nice to have
• would look cool to use entire background as a super picture!

```html
<!DOCTYPE html>
<html lang="en">
<head>
<meta charset="utf-8">
<title>Wecangrowbright – Balanced Nutrition, Mind, and Fitness</title>
<link href="https://fonts.googleapis.com/css2?family=Arimo:wght@400;700&family=Oswald:wght@600&family=PT+Sans:wght@400;700&display=swap" rel="stylesheet">
<style>
:root{
  --orange:#f26a10;
  --orange-light:#ff9a2e;
  --green:#6cb31d;
  --green-deep:#4f9a12;
  --green-soft:#8cc63f;
  --ink:#2b2b2b;
  --text:#3a3a3a;
  --muted:#7a7a7a;
  --nav-top:#5a5a5a;
  --nav-bottom:#262626;
  --panel:#ececec;
  --page:#f3f3f3;
  --line:#d6d6d6;
}
*{box-sizing:border-box;margin:0;padding:0}
html,body{width:960px;height:1200px;overflow:hidden;background:#fff}
body{font-family:"Arimo",Arial,sans-serif;color:var(--text)}
.page{position:relative;width:960px;height:1200px;overflow:hidden}
.abs{position:absolute}
.sheet{left:52px;top:0;width:856px;height:1200px;background:linear-gradient(#f5f5f5,#ededed 120px,#f2f2f2 380px,#f2f2f2)}
.green-band{left:52px;top:380px;width:856px;height:324px;background:linear-gradient(#f2f2f2,#cfe7ad 45%,var(--green-soft) 80%,#7fbd32)}
.content-panel{left:142px;top:380px;width:671px;height:530px;background:linear-gradient(#ececec,#ececec 140px,#fafafa 170px,#fff 300px,#f6f6f6);border-radius:6px 6px 0 0}
.col-rule{width:1px;background:linear-gradient(rgba(0,0,0,.05),rgba(0,0,0,.09),rgba(0,0,0,0));}

/* header */
.brand{left:144px;top:18px;display:flex;align-items:center;gap:8px}
.brand-dot{width:46px;height:46px;border-radius:50%;background:var(--green)}
.brand-name{font-size:23px;color:var(--ink);font-weight:400;letter-spacing:-.2px}
.brand-tag{left:198px;top:55px;font-size:6.5px;letter-spacing:.3px;color:#555}
.promo{left:646px;top:26px;font-size:9px;color:var(--orange);transform:rotate(-5deg);transform-origin:left}
.hh-form{left:740px;top:42px;width:72px;height:15px;border-radius:8px;background:#f3f8ea;border:1px solid #d8e8c2;font-size:8px;font-weight:700;color:var(--green);text-align:center;line-height:13px}
.search{left:630px;top:62px;width:183px;height:20px;background:#fff;border:1px solid #d2d2d2;border-radius:2px;font-size:9px;color:#aaa;padding:4px 7px}
.search svg{position:absolute;right:3px;top:2px}

/* navigation */
.nav{left:52px;top:92px;width:856px;height:31px;background:linear-gradient(var(--nav-top),#3a3a3a 50%,var(--nav-bottom))}
.nav-item{position:absolute;top:0;height:31px;line-height:31px;font-size:9.6px;font-weight:700;color:#fff;white-space:nowrap}
.nav-sep{position:absolute;top:0;width:1px;height:31px;background:#1c1c1c;box-shadow:1px 0 0 #5c5c5c}
.home-tab{left:144px;top:84px;width:52px;height:59px}
.home-tab span{position:absolute;left:0;top:16px;width:52px;text-align:center;font-size:9.6px;font-weight:700;color:var(--green-deep)}

/* hero */
.hero-bg{left:142px;top:123px;width:671px;height:277px;background:radial-gradient(ellipse at 40% 40%,#ffffff,#f1f1f1 60%,#ececec)}
.hero-title{left:168px;top:167px;font-family:"Oswald",sans-serif;font-weight:600;font-size:20px;letter-spacing:-.6px;color:#2a2a2a}
.hero-sub{left:168px;top:198px;font-family:"PT Sans",sans-serif;font-size:11.5px;color:var(--orange);letter-spacing:.1px}
.hero-sub2{left:168px;top:215px;font-family:"PT Sans",sans-serif;font-size:9.6px;line-height:13px;color:var(--orange)}
.arrow{top:228px}
.hero-photo{left:416px;top:144px;width:190px;height:172px;border-radius:50% 50% 8px 8px / 30% 30% 8px 8px;background:linear-gradient(#e8e2dc,#cfc3bb 60%,#b7a3d8)}
.veg-band{left:142px;top:318px;width:502px;height:80px;border-radius:40px 40px 0 0;background:linear-gradient(90deg,#d8b77c,#7da83a 25%,#c8432b 42%,#9bbf55 60%,#4f8c2a 85%,#7bab3f)}

/* diet profile */
.diet{left:648px;top:144px;width:166px;height:228px;background:#e6e6e6;border:2px solid #cfcfcf;border-radius:6px;box-shadow:0 1px 3px rgba(0,0,0,.15)}
.diet-head{height:24px;background:linear-gradient(var(--orange-light),var(--orange));border-radius:4px 4px 0 0;color:#fff;font-size:9px;text-align:center;line-height:24px}
.diet-head b{font-size:11px}
.field{position:absolute;font-size:8px;color:#555}
.select{position:absolute;height:16px;background:#fff;border:1px solid #c9c9c9}
.select::after{content:"";position:absolute;right:0;top:0;width:13px;height:14px;background:#f4f4f4;border-left:1px solid #ddd}
.select i{position:absolute;right:3px;top:5px;width:0;height:0;border:4px solid transparent;border-top:5px solid var(--green-deep);z-index:1}
.radio{position:absolute;width:7px;height:7px;border-radius:50%;border:1px solid #999;background:#fff}
.radio.on::after{content:"";position:absolute;left:1px;top:1px;width:3px;height:3px;border-radius:50%;background:var(--orange)}
.cta{left:22px;width:124px;height:17px;border-radius:9px;background:linear-gradient(var(--orange-light),var(--orange));color:#fff;font-size:8.8px;font-weight:700;text-align:center;line-height:17px;position:absolute}

/* boxes row */
.box-title{position:absolute;font-size:12px;font-weight:700;color:var(--orange)}
.box-icon{position:absolute;width:22px;height:24px;border-radius:3px}
.small{position:absolute;font-size:8.6px;line-height:13.4px;text-align:justify;color:#444}
.more{position:absolute;font-size:8px;font-weight:700;color:#222;text-decoration:underline}
.more::after{content:" »";color:var(--orange-light);text-decoration:none;display:inline-block;margin-left:3px}
.blog-item{position:absolute;left:378px;width:200px}
.blog-thumb{position:absolute;left:0;top:0;width:33px;height:28px;background:linear-gradient(135deg,#6a4c3c,#b38a6a,#3d3d3d)}
.blog-date{position:absolute;left:41px;top:0;font-size:8px;font-weight:700;color:#222}
.blog-text{position:absolute;left:40px;top:12px;width:165px;font-size:7.8px;line-height:9.4px;color:#8a8a8a}
.input{position:absolute;height:15px;background:#fff;border:1px solid #cfcfcf;font-size:7.6px;color:#999;padding:2px 4px}
.go{position:absolute;left:766px;top:432px;width:34px;height:15px;background:var(--green-deep);color:#fff;font-size:9px;font-weight:700;text-align:center;line-height:15px}
.login-note{position:absolute;left:602px;top:452px;width:196px;font-size:9px;line-height:16px;color:#555;text-align:justify;word-spacing:2px}
.login-note a{color:var(--green-deep);font-weight:700;text-decoration:underline}

/* columns */
.col-title{position:absolute;font-size:16.5px;font-weight:700;color:var(--green)}
.video{left:168px;top:593px;width:180px;height:114px;border:3px solid #d8d8d8;background:#222;box-shadow:0 3px 4px rgba(0,0,0,.15)}
.video-frame{position:absolute;left:2px;top:2px;width:170px;height:96px;background:linear-gradient(100deg,#3b2a22,#7a5a48 45%,#5b3d30)}
.video-play{position:absolute;left:82px;top:42px;width:18px;height:18px;background:rgba(0,0,0,.7)}
.video-play::after{content:"";position:absolute;left:6px;top:4px;border:5px solid transparent;border-left:7px solid #fff}
.video-bar{position:absolute;left:0;bottom:0;width:174px;height:10px;background:#333}
.video-bar::after{content:"";position:absolute;left:28px;top:4px;width:110px;height:2px;background:#666}
.mission{position:absolute;left:377px;top:590px;width:200px;font-size:8.7px;line-height:16px;text-align:justify;color:#333}
.mission-link{position:absolute;left:377px;top:768px;font-size:8.7px;color:#222;text-decoration:underline}
.mission-link::after{content:" »";text-decoration:none;display:inline-block;margin-left:2px}
.testi{position:absolute;left:606px;width:189px;font-size:8.6px;line-height:13.4px;text-align:justify;color:#333}
.testi b{color:#222}
.faint{position:absolute;opacity:.55}

/* lower */
.lower-bg{left:142px;top:900px;width:671px;height:210px;background:linear-gradient(#f8f8f8,#eeeeee 30%,#f4f4f4)}
.lower-title{position:absolute;font-size:16px;font-weight:700;color:var(--orange);white-space:nowrap}
.lower-text{position:absolute;font-size:8.4px;line-height:13.6px;text-align:justify;color:#444}

/* footer */
.footer-line{left:52px;top:1109px;width:856px;height:2px;background:var(--green)}
.footer-text{position:absolute;left:52px;width:856px;text-align:center;font-size:8px;color:#333}
.social{position:absolute;top:1162px;width:25px;height:25px;border-radius:50%}
</style>
</head>
<body>
<div class="page">
  <div class="abs sheet"></div>
  <div class="abs green-band"></div>

  <!-- header -->
  <div class="abs brand"><span class="brand-dot"></span><span class="brand-name">Wecangrowbright</span></div>
  <div class="abs brand-tag">BALANCED NUTRITION, MIND, AND FITNESS</div>
  <div class="abs promo">The fastest way to get a new life</div>
  <svg class="abs" style="left:786px;top:20px" width="20" height="22" viewBox="0 0 20 22"><path d="M6 0h8v10h6L10 22 0 10h6z" fill="#7cc12a"/></svg>
  <div class="abs hh-form">Fill up HH form</div>
  <div class="abs search">Search:
    <svg width="15" height="15" viewBox="0 0 15 15"><circle cx="6" cy="6" r="4.5" fill="none" stroke="#f39a1e" stroke-width="2"/><path d="M9.5 9.5l4 4" stroke="#f39a1e" stroke-width="2.4" stroke-linecap="round"/></svg>
  </div>

  <!-- navigation -->
  <nav class="abs nav">
    <span class="nav-item" style="left:162px">Your coaching program</span>
    <span class="nav-sep" style="left:281px"></span>
    <span class="nav-item" style="left:295px">Why a health coach</span>
    <span class="nav-sep" style="left:398px"></span>
    <span class="nav-item" style="left:412px">About your coach</span>
    <span class="nav-sep" style="left:506px"></span>
    <span class="nav-item" style="left:521px">Recipe</span>
    <span class="nav-sep" style="left:566px"></span>
    <span class="nav-item" style="left:582px">Body &amp; Mind workouts</span>
    <span class="nav-sep" style="left:696px"></span>
    <span class="nav-item" style="left:712px">Contact Us</span>
  </nav>
  <div class="abs home-tab">
    <svg width="52" height="59" viewBox="0 0 52 59"><path d="M0 0h52v59L26 47 0 59z" fill="#f39200"/><path d="M0 0h52v8H0z" fill="#f7b500"/></svg>
    <span>Home</span>
  </div>

  <!-- hero -->
  <div class="abs hero-bg"></div>
  <div class="abs hero-title">UT VARIUS IACULIS RHONCUS</div>
  <div class="abs hero-sub">SUSCIPIT SED MATTIS ET, GRAVIDA A TELLUS</div>
  <div class="abs hero-sub2">ALIQUAM PELLENTESQUE ALIQUAM<br>LECTUS AC TEMPOR.</div>
  <svg class="abs arrow" style="left:142px" width="14" height="36" viewBox="0 0 14 36"><path d="M12 0L2 18l10 18" fill="none" stroke="#8cc63f" stroke-width="4"/></svg>
  <svg class="abs arrow" style="left:624px" width="14" height="36" viewBox="0 0 14 36"><path d="M2 0l10 18L2 36" fill="none" stroke="#8cc63f" stroke-width="4"/></svg>
  <div class="abs hero-photo" role="img" aria-label="Photo of a smiling woman sitting cross-legged on a purple yoga mat"></div>
  <div class="abs veg-band" role="img" aria-label="Photo of fresh vegetables: crackers, berries, tomatoes, cabbage, carrots, broccoli and greens"></div>

  <!-- diet profile -->
  <div class="abs diet">
    <div class="diet-head">Get Your Free <b>Diet</b> Profile</div>
    <span class="field" style="left:8px;top:49px">Height</span>
    <span class="select" style="left:38px;top:44px;width:45px"><i></i></span>
    <span class="field" style="left:86px;top:49px">ft.</span>
    <span class="select" style="left:99px;top:44px;width:45px"><i></i></span>
    <span class="field" style="left:147px;top:49px">in.</span>
    <span class="field" style="left:8px;top:79px">Weight</span>
    <span class="select" style="left:38px;top:74px;width:45px"><i></i></span>
    <span class="field" style="left:86px;top:79px">kg.</span>
    <span class="field" style="left:8px;top:104px">Gender</span>
    <span class="radio on" style="left:40px;top:105px"></span>
    <span class="field" style="left:51px;top:104px;color:#888">Male</span>
    <span class="radio" style="left:82px;top:105px"></span>
    <span class="field" style="left:93px;top:104px;color:#888">Female</span>
    <span class="field" style="left:10px;top:126px;line-height:9.4px">Target<br>Weight</span>
    <span class="select" style="left:38px;top:127px;width:45px"><i></i></span>
    <span class="field" style="left:86px;top:131px">kg.</span>
    <span class="field" style="left:10px;top:159px">Age</span>
    <span class="select" style="left:38px;top:154px;width:45px"><i></i></span>
    <div class="cta" style="top:190px">Get Started Now</div>
  </div>

  <!-- content panel -->
  <div class="abs content-panel"></div>
  <div class="abs col-rule" style="left:366px;top:400px;height:500px"></div>
  <div class="abs col-rule" style="left:590px;top:400px;height:500px"></div>

  <!-- health history -->
  <svg class="box-icon" style="left:150px;top:398px" width="22" height="26" viewBox="0 0 22 26"><rect x="1" y="1" width="20" height="24" rx="2" fill="#fff" stroke="#9ab" /><path d="M5 7h12M5 11h12M5 15h12M5 19h8" stroke="#7aa" stroke-width="1.4"/></svg>
  <div class="box-title" style="left:180px;top:411px">Health History Form</div>
  <p class="small" style="left:181px;top:432px;width:172px">Lorem ipsum dolor sit amet, consectetur adipisicing elit, sed do eiusmod tempor incididunt ut labore et dolore magna aliqua. Ut enim ad minim veniam, quis nostrud</p>
  <a class="more" style="left:301px;top:502px">View more</a>

  <!-- blog -->
  <svg class="box-icon" style="left:375px;top:404px" width="28" height="22" viewBox="0 0 28 22"><path d="M2 7l14-6v18L2 13z" fill="#eef3fa" stroke="#5a8ac0" stroke-width="1.4"/><rect x="16" y="6" width="8" height="8" fill="#5a8ac0"/></svg>
  <div class="box-title" style="left:411px;top:411px">Blog</div>
  <div class="blog-item" style="top:435px">
    <div class="blog-thumb" role="img" aria-label="Thumbnail of a music video crowd scene"></div>
    <div class="blog-date">July 27, 2012</div>
    <div class="blog-text">New Lena Hart music video is released w/ Tessa skating!</div>
  </div>
  <div class="blog-item" style="top:474px">
    <div class="blog-thumb" role="img" aria-label="Thumbnail of a skating video still"></div>
    <div class="blog-date">July 27, 2012</div>
    <div class="blog-text">New Lena Hart music video is<br>released w/ Tessa skating!</div>
  </div>
  <a class="more" style="left:526px;top:509px">View more</a>

  <!-- client login -->
  <svg class="box-icon" style="left:602px;top:402px" width="26" height="24" viewBox="0 0 26 24"><circle cx="12" cy="12" r="10" fill="#d9d9d9" stroke="#999"/><text x="12" y="16" font-size="12" text-anchor="middle" fill="#777" font-family="Arial">@</text></svg>
  <div class="box-title" style="left:634px;top:411px">Client Login</div>
  <div class="input" style="left:602px;top:432px;width:80px">User Name:</div>
  <div class="input" style="left:685px;top:432px;width:79px">Password:</div>
  <div class="go">Go</div>
  <p class="login-note">get your free login to access to monthly newsletter and archived articles <a>Register</a></p>

  <!-- featured video -->
  <div class="col-title" style="left:168px;top:561px">Featured Video</div>
  <div class="abs video">
    <div class="video-frame" role="img" aria-label="Video still of a smiling woman in front of a brick wall"></div>
    <div class="video-play"></div>
    <div class="video-bar"></div>
  </div>
  <p class="small" style="left:161px;top:726px;width:190px">Lorem ipsum dolor sit amet, consectetur adipisicing elit, sed do eiusmod tempor incididunt ut labore et dolore magna aliqua. Ut enim ad</p>
  <div class="faint" style="left:192px;top:772px;width:116px;height:130px;border-radius:50% 50% 6px 6px;background:linear-gradient(#e6e6e6,#f4f4f4)" role="img" aria-label="Faint illustration of a film reel and film strip"></div>

  <!-- mission -->
  <div class="col-title" style="left:374px;top:561px">Mission Statement</div>
  <p class="mission">Lorem ipsum dolor sit amet, consectetur adipisicing elit, sed do eiusmod tempor incididunt ut labore et dolore magna aliqua. Ut enim ad minim veniam, quis nostrud exercitation ullamco laboris nisi ut aliquip ex ea commodo consequat. Duis aute irure dolor in reprehenderit in voluptate velit esse cillum dolore eu fugiat nulla pariatur. Excepteur sint occaecat cupidatat non proident, Excepteur sint occaecat cupidatat non proident, sunt in culpa qui officia deserunt mollit anim id est laborum sunt in culpa qui officia deserunt mollit anim id est laborum.</p>
  <a class="mission-link">Contact your health coach</a>
  <div class="faint" style="left:422px;top:804px;width:92px;height:92px;background:linear-gradient(#f2f2f2,#f0dada 60%,#f6f6f6)" role="img" aria-label="Illustration of a hand touching a rising red bar chart"></div>

  <!-- testimonials -->
  <div class="col-title" style="left:602px;top:563px">Testimonials</div>
  <p class="testi" style="top:592px">Lorem ipsum dolor sit amet, consectetur adipisicing elit, sed do eiusmod tempor incididunt ut labore et dolore magna aliqua. Ut enim ad minim veniam, quis nostrud exercitation ullamco laboris nisi ut aliquip ex ea commodo consequat.<br><b>Mara Ellison, Director</b></p>
  <p class="testi" style="top:700px">Lorem ipsum dolor sit amet, consectetur adipisicing elit, sed do eiusmod tempor incididunt ut labore et dolore magna aliqua. Ut enim ad minim veniam, quis nostrud exercitation ullamco laboris nisi ut aliquip ex ea commodo consequat.<br><b>Mara Ellison, Director</b></p>
  <a class="more" style="left:734px;top:816px">View more</a>
  <div class="abs" style="left:596px;top:836px;width:216px;height:80px;background:linear-gradient(#fbfbfb,#ecd2bf 60%,#e2b99c)" role="img" aria-label="Photo of a row of hands giving thumbs up"></div>

  <!-- lower -->
  <div class="abs lower-bg"></div>
  <div class="lower-title" style="left:154px;top:980px">Wecangrowbright Community</div>
  <div class="abs" style="left:410px;top:950px;width:82px;height:52px;border-radius:20px;background:linear-gradient(90deg,#7b5cc4,#e04a3a,#f2b33a,#4bb34b)" role="img" aria-label="Illustration of colourful figures holding hands in a circle"></div>
  <p class="lower-text" style="left:156px;top:1008px;width:416px">Lorem ipsum dolor sit amet, consectetur adipisicing elit, sed do eiusmod tempor incididunt ut labore et dolore magna aliqua. Ut enim ad minim veniam, quis nostrud exercitation ullamco laboris nisi ut aliquip ex ea commodo consequat. Duis aute irure dolor in reprehenderit in voluptate velit esse cillum dolore eu fugiat nulla pariatur. Excepteur sint occaecat cupidatat non proident, Excepteur sint occaecat cupidatat non proident, sunt in culpa qui officia deserunt mollit anim id est laborum sunt in culpa qui officia deserunt mollit anim id est laborum.</p>
  <div class="lower-title" style="left:596px;top:980px">Calender</div>
  <div class="abs" style="left:684px;top:952px;width:72px;height:50px;background:linear-gradient(#d9322c 0,#d9322c 22%,#f7f7f7 22%,#e2e2e2);transform:rotate(-5deg)" role="img" aria-label="Illustration of a wall calendar"></div>
  <p class="lower-text" style="left:598px;top:1008px;width:205px">Lorem ipsum dolor sit amet, consectetur adipisicing elit, sed do eiusmod tempor incididunt ut labore et dolore magna aliqua. Ut enim ad minim veniam, quis nostrud exercitation ullamco laboris nisi ut aliquip ex ea commodo consequat. Duis aute irure dolor in</p>

  <!-- footer -->
  <div class="abs footer-line"></div>
  <p class="footer-text" style="top:1127px">Copyright © 2012, wecangrowbright, All rights reserved!</p>
  <p class="footer-text" style="top:1144px">Contact Us: hello@wecangrowbright.org Phone: 555-014-2271</p>
  <span class="social" style="left:412px;background:#3fa9e0"></span>
  <span class="social" style="left:442px;background:#2a7fc0"></span>
  <span class="social" style="left:472px;background:#2b5aa8"></span>
  <span class="social" style="left:502px;background:#f07a1e"></span>
</div>
</body>
</html>
```